Corrigan Architecture (business card)

We need a business card design. We are a full service architectural firm that specializes in mostly residential projects and some commercial projects. We are located in Hudson Valley, New York. We work with high end clients and want a business card that is memorable and has a sleek, modern, design but will not go out of style (timeless).

Target Market(s)

high end residential clients

Industry/Entity Type

Architect

Contact Information for Business Card

Front of card
Company Logo
website: www.corriganarchitectur.example
what we do: residential, Commercial

back of card
Owner's Name: Dorian Corrigan
owner's title: Principal
Business address: 2873 Route 92 Suite A, Brellfordton, NY 12688
phone number: 845-608-2917
e-mail: dc@corriganarchitecture.example

We like:
icons
sleek and clean design
simple not too busy or too much text

Font styles to use
Sans Serif

Colors
0356a4

Requirements
Must have
• company colors are navy blue, white, and gray
• Front of card
• Company Logo
• website: www.corriganarchitectur.example
• what we do: residential, Commercial
• back of card
• Owner's Name: Dorian Corrigan
• owner's title: Principal
• Business address: 2873 Route 92 Suite A, Brellfordton, NY 12688
• phone number: 845-608-2917
• e-mail: dc@corriganarchitecture.example
Nice to have
• We like:
• icons
• sleek and clean design
• simple not too much text
• color of the card to be either blue or gray
Should not have
• we do not like houses in the design or plans of houses-this is over done and we don't like it.
• no QR CODES

```html
<!DOCTYPE html>
<html lang="en">
<head>
<meta charset="utf-8">
<title>Corrigan Architecture — Business Card</title>
<link rel="stylesheet" href="https://fonts.googleapis.com/css2?family=Open+Sans:wght@400;700&display=swap">
<style>
  :root {
    --backdrop: #606060;
    --navy: #22215f;
    --white: #ffffff;
    --gray: #7a7a7a;
  }
  * { margin: 0; padding: 0; box-sizing: border-box; }
  html, body {
    width: 1200px; height: 1000px; overflow: hidden;
    background: var(--backdrop);
    font-family: "Open Sans", Arial, sans-serif;
  }
  .canvas { position: relative; width: 1200px; height: 1000px; }

  .card { position: absolute; overflow: hidden; }

  /* Contact side */
  .card-contact {
    left: 243px; top: 81px; width: 715px; height: 408px;
    background: var(--white);
  }
  .brand {
    position: absolute; left: 140px; top: 48px;
    display: flex; align-items: center; gap: 16px;
  }
  .brand-square { width: 30px; height: 30px; background: var(--gray); }
  .brand-name {
    color: var(--navy); font-weight: 400; font-size: 32px;
    line-height: 38px; letter-spacing: 1px; text-transform: uppercase;
  }
  .person-name {
    position: absolute; left: 140px; top: 160px;
    color: var(--navy); font-weight: 700; font-size: 25px; letter-spacing: 2.5px;
    text-transform: uppercase;
  }
  .person-title {
    position: absolute; left: 140px; top: 191px;
    color: var(--navy); font-size: 17px; letter-spacing: 2px; text-transform: uppercase;
  }
  .contact-line {
    position: absolute; left: 140px;
    display: flex; align-items: center; gap: 12px;
    color: var(--navy); font-size: 18px; text-transform: uppercase;
  }
  .contact-phone { top: 246px; letter-spacing: 4px; }
  .contact-email { top: 290px; letter-spacing: 2.6px; }
  .contact-line svg { flex: none; fill: var(--navy); }

  .address-band {
    position: absolute; left: 0; bottom: 0; width: 100%; height: 74px;
    background: var(--navy);
    display: flex; align-items: center; justify-content: center; gap: 12px;
    color: var(--white); font-size: 19px; text-transform: uppercase;
  }
  .address-band svg { fill: var(--white); margin-top: -6px; }

  /* Brand side */
  .card-brand {
    left: 242px; top: 510px; width: 715px; height: 409px;
    background: var(--navy); color: var(--white); text-align: center;
  }
  .brand-feature {
    position: absolute; left: 0; top: 110px; width: 100%;
    display: flex; flex-direction: column; align-items: center; gap: 18px;
  }
  .brand-feature .brand-square { background: var(--white); width: 34px; height: 34px; }
  .brand-feature .brand-name { color: var(--white); font-size: 34px; line-height: 42px; letter-spacing: 2px; }
  .services {
    position: absolute; left: 0; top: 277px; width: 100%;
    font-size: 19px; text-transform: uppercase;
  }
  .website {
    position: absolute; left: 0; top: 357px; width: 100%;
    font-size: 19px; text-transform: uppercase;
  }
</style>
</head>
<body>
<main class="canvas">

  <section class="card card-contact">
    <div class="brand">
      <span class="brand-square"></span>
      <p class="brand-name">Corrigan<br>Architecture</p>
    </div>
    <h1 class="person-name">Dorian Corrigan</h1>
    <p class="person-title">Principal</p>

    <p class="contact-line contact-phone">
      <svg width="24" height="24" viewBox="0 0 24 24" aria-hidden="true">
        <path d="M6.6 10.8c1.4 2.8 3.8 5.1 6.6 6.6l2.2-2.2c.3-.3.7-.4 1-.2 1.1.4 2.3.6 3.6.6.6 0 1 .4 1 1V20c0 .6-.4 1-1 1C10.6 21 3 13.4 3 4c0-.6.4-1 1-1h3.5c.6 0 1 .4 1 1 0 1.2.2 2.4.6 3.6.1.3 0 .7-.2 1l-2.3 2.2z"/>
        <path d="M14 2.5a8 8 0 0 1 7.5 7.5h-1.6A6.4 6.4 0 0 0 14 4.1zM14 5.8a4.8 4.8 0 0 1 4.2 4.2h-1.6A3.2 3.2 0 0 0 14 7.4z"/>
      </svg>
      845-608-2917
    </p>
    <p class="contact-line contact-email">
      <svg width="24" height="16" viewBox="0 0 24 16" aria-hidden="true">
        <path d="M0 0h24v16H0z M1.5 1.5v.6L12 9l10.5-6.9v-.6z" fill-rule="evenodd"/>
      </svg>
      dc@corriganarchitecture.example
    </p>

    <div class="address-band">
      <svg width="18" height="28" viewBox="0 0 18 28" aria-hidden="true">
        <path d="M9 0a9 9 0 0 0-9 9c0 6.8 9 19 9 19s9-12.2 9-19a9 9 0 0 0-9-9zm0 12.5A3.5 3.5 0 1 1 9 5.5a3.5 3.5 0 0 1 0 7z"/>
      </svg>
      <span>2873 Route 92 Suite A, Brellfordton, NY 12688</span>
    </div>
  </section>

  <section class="card card-brand">
    <div class="brand-feature">
      <span class="brand-square"></span>
      <p class="brand-name">Corrigan Architecture</p>
    </div>
    <p class="services">Residential &amp; Commercial</p>
    <p class="website">www.corriganarchitectur.example</p>
  </section>

</main>
</body>
</html>
```